Tozvar new design for business cards we want to change our existing design. Logo must remain the same

Hello we are the company TozVar and offer various services regarding transportation and disposal. In addition to our main acquisition of van rental, we also offer disposal and express transportation, so we need new business card designs for our business. Our elders have their time and do not like it anymore. We want to change our existing design. Logo must remain the same as well as the color blue, whether dark or light Does not play a big role in the best medium blue. Logo must be present on the front side. As well as telephone, email, web and location. Big enough but not too big. Back can be redesigned Logo as well as name TozVar must be present. Important is the text: Van rental Disposal and clearing express transportation. Without bail in red should be noted somewhere. it should be modern but not too playful. rather serious but no beating company Thank you very much

Target Market(s)

Private customers as well as companies we want to change our existing design. Logo must remain the same as well as the color blue, whether dark or light Does not play a big role in the best medium blue. Logo must be present on the front side. As well as telephone, email, web and location. Big enough but not too big. Back can be redesigned Logo as well as name TozVar must be present. Important is the text: Van rental Disposal and clearing express transportation. Without bail in red should be noted somewhere. it should be modern but not too playful. rather serious but no beating company Thank you very much

Industry/Entity Type

Car Rental

Contact Information for Business Card

we want to change our existing design. Logo must remain the same as well as the color blue, whether dark or light Does not play a big role in the best medium blue.
Logo must be present on the front side.
As well as telephone, email, web and location. Big enough but not too big.
Back can be redesigned Logo as well as name TozVar must be present.
Important is the text:
Van rental
Disposal and clearing
Express transportation.
Without bail in red should be noted somewhere.
it should be modern but not too playful. rather serious but no beating company
Thank you very much

Font styles to use
Sans Serif

Colors
33a6d7
ec1f27
0692cd
3277b5

Requirements
Must have
• logo and name TozVar as described in the above text must have it. we want to change our existing design. Logo must remain the same as well as the color blue, whether dark or light Does not play a big role in the best medium blue. Logo must be present on the front side. As well as telephone, email, web and location. Big enough but not too big. Back can be redesigned Logo as well as name TozVar must be present. Important is the text: Van rental Disposal and clearing express transportation. Without bail in red should be noted somewhere. it should be modern but not too playful. rather serious but no beating company Thank you very much
Nice to have
• see description we want to change our existing design. Logo must remain the same as well as the color blue, whether dark or light Does not play a big role in the best medium blue. Logo must be present on the front side. As well as telephone, email, web and location. Big enough but not too big. Back can be redesigned Logo as well as name TozVar must be present. Important is the text: Van rental Disposal and clearing express transportation. Without bail in red should be noted somewhere. it should be modern but not too playful. rather serious but no beating company Thank you very much
Should not have
• Blue White and little red we want to change our existing design. Logo must remain the same as well as the color blue, whether dark or light Does not play a big role in the best medium blue. Logo must be present on the front side. As well as telephone, email, web and location. Big enough but not too big. Back can be redesigned Logo as well as name TozVar must be present. Important is the text: Van rental Disposal and clearing express transportation. Without bail in red should be noted somewhere. it should be modern but not too playful. rather serious but no beating company Thank you very much

```html
<!DOCTYPE html>
<html lang="en">
<head>
<meta charset="utf-8">
<title>Tozvar GmbH – Business Card</title>
<link rel="stylesheet" href="https://fonts.googleapis.com/css2?family=Lato:wght@400;700;900&display=swap">
<style>
  :root {
    --backdrop: #2b2b2e;
    --royal: #15159a;
    --navy: #1c1c78;
    --steel: #6f8ca6;
    --ink-soft: #3a3a44;
    --rule: #55555c;
    --paper: #f7f7f8;
    --white: #ffffff;
    --alert: #ec1f27;
  }
  * { box-sizing: border-box; margin: 0; padding: 0; }
  html, body {
    width: 1200px; height: 997px; overflow: hidden;
    background: var(--backdrop);
    font-family: "Lato", Arial, sans-serif;
  }
  .stage {
    width: 1200px; height: 997px;
    display: flex; flex-direction: column;
    align-items: center; justify-content: center; gap: 48px;
  }
  .card {
    width: 760px; height: 434px; position: relative;
    border-radius: 4px; box-shadow: 0 10px 30px rgba(0,0,0,.45);
  }

  /* Wordmark */
  .wordmark { display: flex; align-items: center; gap: 22px; }
  .wordmark__mark { display: block; }
  .wordmark__name { font-weight: 900; letter-spacing: 2px; line-height: 1; }

  /* Back side */
  .card--back {
    background: var(--royal);
    display: flex; flex-direction: column; align-items: center; justify-content: center;
  }
  .card--back .wordmark__name { color: var(--white); font-size: 92px; }
  .card--back .wordmark__mark { width: 70px; height: 70px; background: var(--white); }
  .services {
    list-style: none; display: flex; gap: 14px; margin-top: 34px;
    font-size: 19px; font-weight: 700; color: var(--white); letter-spacing: .5px;
  }
  .services__item + .services__item::before { content: "·"; margin-right: 14px; }
  .services__note {
    margin-top: 18px; padding: 6px 16px; background: var(--alert);
    color: var(--white); font-size: 16px; font-weight: 900; letter-spacing: 1.5px; text-transform: uppercase;
  }

  /* Front side */
  .card--front { background: var(--paper); border-bottom: 8px solid var(--royal); }
  .card--front .wordmark { position: absolute; left: 60px; top: 56px; }
  .card--front .wordmark__name { color: var(--navy); font-size: 62px; }
  .card--front .wordmark__mark { width: 50px; height: 50px; background: var(--navy); }

  .holder { position: absolute; left: 60px; top: 228px; text-align: right; width: 270px; }
  .holder__name { font-size: 24px; color: var(--navy); font-weight: 400; letter-spacing: .5px; }
  .holder__name strong { font-weight: 900; }
  .holder__role { font-size: 18px; color: var(--ink-soft); margin-top: 4px; }
  .holder__web { font-size: 19px; font-weight: 900; color: var(--navy); margin-top: 40px; letter-spacing: .5px; }

  .divider { position: absolute; left: 362px; top: 172px; width: 3px; height: 172px; background: var(--rule); }
  .contacts {
    position: absolute; left: 392px; top: 174px; list-style: none;
    display: flex; flex-direction: column; gap: 14px;
  }
  .contacts__item { display: flex; align-items: center; gap: 14px; font-size: 19px; color: var(--ink-soft); letter-spacing: .5px; }
  .contacts__icon {
    width: 28px; height: 28px; border-radius: 50%; background: var(--navy);
    display: flex; align-items: center; justify-content: center; flex: none;
  }
  .contacts__icon svg { width: 16px; height: 16px; fill: var(--white); }
  .front-note {
    position: absolute; right: 60px; bottom: 30px;
    font-size: 14px; font-weight: 900; color: var(--alert); letter-spacing: 1px; text-transform: uppercase;
  }
</style>
</head>
<body>
<main class="stage">
  <section class="card card--back" aria-label="Card back">
    <div class="wordmark">
      <span class="wordmark__mark" aria-hidden="true"></span>
      <span class="wordmark__name">TOZVAR</span>
    </div>
    <ul class="services">
      <li class="services__item">Van rental</li>
      <li class="services__item">Disposal and clearing</li>
      <li class="services__item">Express transportation</li>
    </ul>
    <p class="services__note">Without bail</p>
  </section>

  <section class="card card--front" aria-label="Card front">
    <div class="wordmark">
      <span class="wordmark__mark" aria-hidden="true"></span>
      <span class="wordmark__name">TOZVAR</span>
    </div>

    <div class="holder">
      <p class="holder__name">MAREN <strong>KOVALSKY</strong></p>
      <p class="holder__role">Founder and CEO</p>
      <p class="holder__web">www.tozvar.com</p>
    </div>

    <div class="divider" aria-hidden="true"></div>

    <ul class="contacts">
      <li class="contacts__item">
        <span class="contacts__icon" aria-hidden="true">
          <svg viewBox="0 0 24 24"><path d="M6.6 10.8a15.1 15.1 0 0 0 6.6 6.6l2.2-2.2c.3-.3.7-.4 1-.2 1.1.4 2.3.6 3.6.6.6 0 1 .4 1 1V20c0 .6-.4 1-1 1A17 17 0 0 1 3 4c0-.6.4-1 1-1h3.5c.6 0 1 .4 1 1 0 1.3.2 2.5.6 3.6.1.3 0 .7-.2 1z"/></svg>
        </span>
        512.555.0142
      </li>
      <li class="contacts__item">
        <span class="contacts__icon" aria-hidden="true">
          <svg viewBox="0 0 24 24"><path d="M3 5h18v14H3z M4.5 6.5 12 12.5l7.5-6z" fill-rule="evenodd"/></svg>
        </span>
        maren@tozvar.com
      </li>
      <li class="contacts__item">
        <span class="contacts__icon" aria-hidden="true">
          <svg viewBox="0 0 24 24"><path d="M10.6 13.4a1 1 0 0 0 1.4 0l4-4a3 3 0 0 0-4.2-4.2l-1.2 1.2 1.4 1.4 1.2-1.2a1 1 0 0 1 1.4 1.4l-4 4a1 1 0 0 0 0 1.4zM13.4 10.6a1 1 0 0 0-1.4 0l-4 4a3 3 0 0 0 4.2 4.2l1.2-1.2-1.4-1.4-1.2 1.2a1 1 0 0 1-1.4-1.4l4-4a1 1 0 0 0 0-1.4z"/></svg>
        </span>
        network.tozvar.com/team
      </li>
      <li class="contacts__item">
        <span class="contacts__icon" aria-hidden="true">
          <svg viewBox="0 0 24 24"><path d="M12 2a7 7 0 0 0-7 7c0 5 7 13 7 13s7-8 7-13a7 7 0 0 0-7-7zm0 9.5A2.5 2.5 0 1 1 12 6.5a2.5 2.5 0 0 1 0 5z"/></svg>
        </span>
        Hafenweg 12, 28197 Bremen
      </li>
    </ul>

    <p class="front-note">Without bail</p>
  </section>
</main>
</body>
</html>
```